Wine label design for my wife. Wine called "The Mirabel"

I need a wine label face lift of one of my premium wines in my collection. My wine sells in Harbor Lark's all over the States. My current label is called The Mirabel (my wife's name) and the illustration of her eyes is done by a well know artist from South Africa. I do not have to use this illustration and therefor I attached several pictures of her and her eyes, even when she was a little girl. The wine's also made in South Africa. This is a premium wine that we only sell 2000 bottles per year. The wine sells at 60 usd per bottle, The current label is too white. I also think her eyes should look more at the person buying it, than away from them.

Target Market(s)

Top end wine buyers

Font styles to use
Decorative
Script

Requirements
Must have
• 'The Mirabel' must be on the label
An illustration must be on the label
Basically all the info that's on the current label must be on by law. As per Sample
Nice to have
• Maybe some ideas of her whole face?
Should not have
• any gold colour

```html
<!DOCTYPE html>
<html lang="en">
<head>
<meta charset="utf-8">
<title>The Mirabel – Sauvignon Blanc 2017 Label</title>
<link href="https://fonts.googleapis.com/css2?family=Great+Vibes&family=Cormorant+Garamond:wght@500;600&display=swap" rel="stylesheet">
<style>
  :root {
    --backdrop: #0c0c0c;
    --label-black: #1b1b1b;
    --label-edge: #141414;
    --wine-red: #c8141b;
    --brand-red: #a8282c;
    --soft-grey: #b9b9b9;
    --ink-white: #f1f1f1;
    --photo-light: #e9e9e9;
    --photo-mid: #bdbdbd;
    --photo-dark: #6a6a6a;
  }
  * { margin: 0; padding: 0; box-sizing: border-box; }
  html, body {
    width: 1200px;
    height: 959px;
    overflow: hidden;
    background: var(--backdrop);
  }
  .canvas {
    position: relative;
    width: 1200px;
    height: 959px;
    background: var(--backdrop);
  }
  .wine-label {
    position: absolute;
    left: 357px;
    top: 60px;
    width: 485px;
    height: 840px;
    background: linear-gradient(180deg, var(--label-black) 0%, #1e1e1e 50%, var(--label-edge) 100%);
    overflow: hidden;
  }
  .wine-name {
    position: absolute;
    left: 10px;
    top: 100px;
    width: 470px;
    text-align: center;
    font-family: "Great Vibes", cursive;
    font-size: 96px;
    line-height: 1;
    color: var(--wine-red);
    transform: rotate(-9deg);
    white-space: nowrap;
  }
  .varietal {
    position: absolute;
    left: 60px;
    top: 252px;
    width: 400px;
    text-align: center;
    font-family: "Cormorant Garamond", serif;
    font-weight: 600;
    font-size: 17px;
    letter-spacing: 5px;
    color: var(--soft-grey);
    transform: rotate(-11deg);
    white-space: nowrap;
  }
  .portrait-strip {
    position: absolute;
    left: 0;
    top: 0;
    width: 485px;
    height: 840px;
  }
  .winery {
    position: absolute;
    left: 0;
    top: 676px;
    width: 485px;
    text-align: center;
    font-family: "Cormorant Garamond", serif;
    font-weight: 500;
    font-size: 30px;
    letter-spacing: 5px;
    color: var(--brand-red);
  }
  .volume {
    position: absolute;
    left: 0;
    top: 738px;
    width: 485px;
    text-align: center;
    font-family: "Cormorant Garamond", serif;
    font-weight: 600;
    font-size: 19px;
    letter-spacing: 1.5px;
    color: var(--ink-white);
    word-spacing: 4px;
  }
</style>
</head>
<body>
<main class="canvas">
  <section class="wine-label">
    <h1 class="wine-name">The Mirabel</h1>
    <p class="varietal">SAUVIGNON BLANC 2017</p>

    <svg class="portrait-strip" viewBox="0 0 485 840" role="img" aria-label="Black and white photograph of a woman's eyes, seen through a torn paper strip">
      <defs>
        <linearGradient id="photoTone" x1="0" y1="0" x2="1" y2="0.3">
          <stop offset="0" stop-color="var(--photo-mid)"/>
          <stop offset="0.3" stop-color="var(--photo-light)"/>
          <stop offset="0.7" stop-color="var(--photo-light)"/>
          <stop offset="0.93" stop-color="var(--photo-mid)"/>
          <stop offset="1" stop-color="var(--photo-dark)"/>
        </linearGradient>
      </defs>
      <polygon fill="url(#photoTone)" points="0,368 18,364 32,366 60,359 78,361 96,354 120,352 138,347 152,348 180,340 204,338 222,333 240,331 262,328 280,322 300,320 326,316 344,311 362,310 388,303 402,304 424,297 446,291 462,288 474,283 485,277 485,522 470,524 458,529 432,533 416,538 398,540 372,546 354,548 338,553 312,556 294,561 278,563 252,568 236,571 216,575 192,580 176,582 158,587 132,591 112,596 98,598 72,604 54,606 38,611 18,613 0,619"/>
    </svg>

    <p class="winery">ALDER VANE WINES</p>
    <p class="volume">750 ml | 13% vol.</p>
  </section>
</main>
</body>
</html>
```